'Bright Ledger Hidden Keys' Book Cover

I need a professional book cover design for my new upcoming book that shows people how to get a high credit score.

Here are my two websites:

https://www.moneywordbank-lexa.info
https://moneywordbank-lexa.com/

I am looking for a clean, professional design that pops (emotional touch) and separates from the other books that are on the market. Cover aspect ratio 1:4 for Pagewisp version and 1:5 for the paperback version. Yellow or blue are good colors - but not must. See the basic examples that I provided. File delivery format PDF.

Book Title: Bright Ledger Hidden Keys
Byline: The Quick Lift And Mend Manual for Stellar Borrowing

Currently on Brindlecart pre-order:
https://www.brindlecart.example/Bright-Ledger-Hidden-Keys-Stellar-ebook/dp/Q48MPLRT71

I am the author of 36 published books on Brindlecart. My author profile is here:
brindlecart.example/author/gideonvarly

Targeted audience: People that want to improve or repair their bad credit score.

Target Market(s)

People/consumers in the US that want to improve or repair their credit score.

Industry/Entity Type

Consumer

Font styles to use
Sans Serif

Colors

Designer to choose colors to be used in the design.

Requirements
Must have
• Author name, Title, byline, and graphic element(s).
Nice to have
• - 2020 edition logo / batch

```html
<!DOCTYPE html>
<html lang="en">
<head>
<meta charset="utf-8">
<title>Bright Ledger Hidden Keys — Book Cover</title>
<link href="https://fonts.googleapis.com/css2?family=Bebas+Neue&family=Jost:wght@500;700&display=swap" rel="stylesheet">
<style>
  :root {
    --canvas: #ececec;
    --sky-deep: #2f86f6;
    --sky-light: #c4e0ff;
    --sun-yellow: #fdc010;
    --ink-navy: #0c0e50;
    --portrait-dark: #6b4a36;
    --portrait-warm: #d9a88a;
  }
  html, body {
    margin: 0;
    padding: 0;
    width: 1200px;
    height: 2335px;
    overflow: hidden;
    background: var(--canvas);
  }
  .canvas {
    position: relative;
    width: 1200px;
    height: 2335px;
  }
  .book-cover {
    position: absolute;
    left: 100px;
    top: 419px;
    width: 1000px;
    height: 1497px;
    overflow: hidden;
    background: radial-gradient(ellipse 55% 40% at 50% 26%, var(--sky-light) 0%, #7fb7ff 45%, var(--sky-deep) 100%);
    box-shadow: 0 6px 24px rgba(0,0,0,0.12);
  }
  .cover-art {
    position: absolute;
    inset: 0;
    width: 100%;
    height: 100%;
  }
  .author-name {
    position: absolute;
    top: 68px;
    left: 0;
    width: 100%;
    margin: 0;
    text-align: center;
    font-family: 'Jost', sans-serif;
    font-weight: 500;
    font-size: 56px;
    letter-spacing: 0.5px;
    color: var(--ink-navy);
  }
  .book-title {
    position: absolute;
    right: 56px;
    top: 948px;
    margin: 0;
    text-align: right;
    font-family: 'Bebas Neue', sans-serif;
    font-weight: 400;
    font-size: 156px;
    line-height: 0.96;
    letter-spacing: 1px;
    color: var(--ink-navy);
  }
  .book-title span { display: block; }
  .book-byline {
    position: absolute;
    right: 56px;
    top: 1290px;
    margin: 0;
    text-align: right;
    font-family: 'Jost', sans-serif;
    font-weight: 700;
    font-size: 44px;
    line-height: 1.18;
    color: var(--ink-navy);
  }
  .book-byline span { display: block; }
</style>
</head>
<body>
<div class="canvas">
  <div class="book-cover">
    <svg class="cover-art" viewBox="0 0 1000 1497" preserveAspectRatio="none">
      <defs>
        <linearGradient id="portraitTone" x1="0" y1="0" x2="0" y2="1">
          <stop offset="0" stop-color="var(--portrait-dark)"/>
          <stop offset="0.45" stop-color="var(--portrait-warm)"/>
          <stop offset="1" stop-color="var(--portrait-dark)"/>
        </linearGradient>
      </defs>
      <path class="portrait-placeholder" role="img"
            aria-label="Smiling young woman with long brown hair peeking over the yellow panel, hands gripping its edge"
            d="M60 1080 C90 900 200 800 290 700 C320 420 420 230 520 220 C640 215 720 330 740 520 L760 560 L890 480 L880 420 L910 400 L930 460 L60 1120 Z"
            fill="url(#portraitTone)" opacity="0.85"/>
      <polygon class="yellow-panel" points="0,1088 1000,329 1000,1497 0,1497" fill="var(--sun-yellow)"/>
    </svg>
    <p class="author-name">GIDEON VARLY</p>
    <h1 class="book-title"><span>BRIGHT LEDGER</span><span>HIDDEN KEYS</span></h1>
    <p class="book-byline"><span>THE QUICK LIFT AND MEND</span><span>MANUAL FOR STELLAR BORROWING</span></p>
  </div>
</div>
</body>
</html>
```